Modern Design Business Card industrial maintenance company

Business card design for Company named Brookvale Equipment Services

Target Market(s)

Industrial

Industry/Entity Type

Maintenance and repair

Contact Information for Business Card

Place holder for address, office phone, mobile number and email

Requirements
Must have
• Clean modern look
Nice to have
• N/a

```html
<!DOCTYPE html>
<html lang="en">
<head>
<meta charset="utf-8">
<title>Brookvale Equipment Services – Business Card</title>
<link rel="stylesheet" href="https://fonts.googleapis.com/css2?family=Montserrat:wght@400;600&family=Open+Sans:wght@400;600&display=swap">
<style>
  :root {
    --ink: #0b0b0b;
    --paper: #ffffff;
    --stage: #e9e7e4;
    --muted: #c9c9c9;
    --pattern-a: #050505;
    --pattern-b: #1c1c1c;
  }
  * { box-sizing: border-box; margin: 0; padding: 0; }
  html, body {
    width: 1200px; height: 1200px; overflow: hidden;
    background: var(--stage);
  }
  .stage {
    position: relative; width: 1200px; height: 1200px;
  }
  .card {
    position: absolute; left: 180px; width: 840px; height: 480px;
    box-shadow: 0 10px 28px rgba(0,0,0,.18);
    overflow: hidden;
  }
  /* Front */
  .card--front { top: 90px; background: var(--ink); }
  .front__pattern {
    position: absolute; inset: 0;
    background: linear-gradient(135deg, var(--pattern-b) 0%, var(--pattern-a) 55%, var(--pattern-b) 100%);
  }
  .front__seal {
    position: absolute; left: 50%; top: 50%;
    width: 210px; height: 210px; margin: -105px 0 0 -105px;
    border-radius: 50%; background: #f1f1f1;
    display: flex; align-items: center; justify-content: center; text-align: center;
  }
  .front__seal-name {
    font-family: "Montserrat", sans-serif; font-weight: 600;
    font-size: 17px; line-height: 1.35; letter-spacing: .12em;
    color: var(--ink); text-transform: uppercase;
  }
  /* Back */
  .card--back { top: 630px; background: var(--paper); }
  .back__tab {
    position: absolute; right: 0; top: 34px;
    width: 78px; height: 44px; background: var(--ink);
  }
  .brand {
    position: absolute; left: 340px; top: 110px;
    display: flex; align-items: center; gap: 14px;
  }
  .brand__dot {
    width: 46px; height: 46px; border-radius: 50%;
    border: 3px solid var(--ink);
  }
  .brand__name {
    font-family: "Montserrat", sans-serif; font-weight: 600;
    font-size: 22px; letter-spacing: .08em; color: var(--ink);
    text-transform: uppercase;
  }
  .person {
    position: absolute; left: 0; top: 200px;
    width: 360px; height: 78px; background: var(--ink);
    padding: 14px 0 0 120px; color: var(--paper);
  }
  .person__name {
    font-family: "Montserrat", sans-serif; font-weight: 400;
    font-size: 23px; letter-spacing: .1em; text-transform: uppercase;
  }
  .person__role {
    font-family: "Montserrat", sans-serif; font-weight: 400;
    font-size: 13px; letter-spacing: .14em; color: var(--muted);
    text-transform: uppercase; margin-top: 2px;
  }
  .contacts {
    position: absolute; left: 120px; top: 318px; list-style: none;
  }
  .contacts__item {
    display: flex; align-items: center; gap: 10px;
    font-family: "Open Sans", sans-serif; font-weight: 600;
    font-size: 21px; letter-spacing: .04em; line-height: 32px; color: var(--ink);
  }
  .contacts__icon {
    width: 18px; height: 18px; flex: none;
  }
</style>
</head>
<body>
<main class="stage">
  <section class="card card--front" aria-label="Card front">
    <div class="front__pattern" role="img" aria-label="Repeating dark monogram pattern on black"></div>
    <div class="front__seal">
      <span class="front__seal-name">Brookvale<br>Equipment<br>Services</span>
    </div>
  </section>

  <section class="card card--back" aria-label="Card back">
    <div class="back__tab"></div>

    <div class="brand">
      <span class="brand__dot"></span>
      <span class="brand__name">Brookvale Equipment Services</span>
    </div>

    <div class="person">
      <p class="person__name">Daniel Hart</p>
      <p class="person__role">Director</p>
    </div>

    <ul class="contacts">
      <li class="contacts__item">
        <svg class="contacts__icon" viewBox="0 0 18 18"><rect width="18" height="18" rx="2" fill="#0b0b0b"/><path d="M5 4l2 0 1 3-1.3 1a6 6 0 003.3 3.3L11 10l3 1v2c-5 .5-9.5-4-9-9z" fill="#fff"/></svg>
        448 5550 1927
      </li>
      <li class="contacts__item">
        <svg class="contacts__icon" viewBox="0 0 18 18"><rect width="18" height="18" rx="2" fill="#0b0b0b"/><rect x="6" y="3" width="6" height="12" rx="1" fill="none" stroke="#fff" stroke-width="1.4"/><circle cx="9" cy="12.5" r=".9" fill="#fff"/></svg>
        448 5550 1927
      </li>
      <li class="contacts__item">
        <svg class="contacts__icon" viewBox="0 0 18 18"><rect width="18" height="18" rx="2" fill="#0b0b0b"/><rect x="3.5" y="5" width="11" height="8" fill="none" stroke="#fff" stroke-width="1.3"/><path d="M3.5 5l5.5 4.5L14.5 5" fill="none" stroke="#fff" stroke-width="1.3"/></svg>
        hello@brookvale-es.com
      </li>
      <li class="contacts__item">
        <svg class="contacts__icon" viewBox="0 0 18 18"><rect width="18" height="18" rx="2" fill="#0b0b0b"/><path d="M9 15s-4-4.3-4-7.5a4 4 0 018 0C13 10.7 9 15 9 15z" fill="#fff"/><circle cx="9" cy="7.5" r="1.5" fill="#0b0b0b"/></svg>
        48 Millrace Rd., Fernbrook, ST 40218
      </li>
    </ul>
  </section>
</main>
</body>
</html>
```